We need visit card and a letter paper for our website. thx

We have a beauty clinic in Switzerland.
https://wolkenbachtal.ch
We need a visit card.

Requirements
Must have
• see colors on website

```html
<!DOCTYPE html>
<html lang="en">
<head>
<meta charset="utf-8">
<title>Wolkenbachtal Beauty Clinic – Business Card</title>
<link rel="stylesheet" href="https://fonts.googleapis.com/css2?family=Montserrat:wght@400;500&display=swap">
<style>
  :root {
    --backdrop: #2f2f31;
    --card: #e9c4d1;
    --ink: #2b2526;
    --accent: #b0193f;
  }
  * { margin: 0; padding: 0; box-sizing: border-box; }
  html, body { width: 1200px; height: 900px; overflow: hidden; }
  body {
    background: var(--backdrop);
    font-family: "Montserrat", Arial, sans-serif;
    color: var(--ink);
    position: relative;
  }
  .card {
    position: absolute;
    top: 100px;
    height: 698px;
    background: var(--card);
  }
  .card--front { left: 178px; width: 400px; }
  .card--back { left: 628px; width: 388px; }
  .line {
    position: absolute;
    left: 0; right: 0;
    text-align: center;
    white-space: nowrap;
    transform: translateY(-50%);
  }
  .holder-name { top: 94px; font-size: 25px; letter-spacing: 1.5px; }
  .holder-title { top: 121px; font-size: 19px; letter-spacing: 0.8px; color: var(--accent); }
  .rule {
    position: absolute;
    left: 50%;
    width: 18px; height: 3px;
    margin-left: -9px;
    background: var(--ink);
  }
  .rule--top { top: 148px; }
  .rule--bottom { top: 609px; }
  .brand-name { font-size: 31px; font-weight: 500; letter-spacing: 0.5px; }
  .card--front .brand-name { top: 264px; }
  .brand-tag { font-size: 12px; letter-spacing: 4px; }
  .card--front .brand-tag { top: 298px; }
  .address { font-size: 17px; letter-spacing: 0.8px; line-height: 1; }
  .address--1 { top: 362px; }
  .address--2 { top: 380px; }
  .address--3 { top: 404px; }
  .address--4 { top: 422px; }
  .contact-icons {
    position: absolute;
    top: 455px; left: 0; right: 0;
    display: flex; justify-content: center; gap: 19px;
  }
  .contact-icons svg { width: 23px; height: 23px; display: block; }
  .contact { font-size: 19px; letter-spacing: 1px; }
  .contact--phone { top: 511px; }
  .contact--mail { top: 544px; }
  .contact--web { top: 578px; }
  .contact--web .domain { color: var(--accent); }
  .card--back .brand-name { top: 332px; }
  .card--back .brand-tag { top: 371px; }
  .card--back .web { top: 417px; font-size: 21px; letter-spacing: 0.8px; }
</style>
</head>
<body>
  <section class="card card--front" aria-label="Business card front">
    <p class="line holder-name">LENA MARWALD</p>
    <p class="line holder-title">Doctor of Medicine</p>
    <div class="rule rule--top"></div>

    <p class="line brand-name">Wolkenbachtal</p>
    <p class="line brand-tag">BEAUTY CLINIC</p>

    <p class="line address address--1">Wolkenbachtal</p>
    <p class="line address address--2">Beauty Clinic Bergün</p>
    <p class="line address address--3">Bachgasse 12, 7482 Bergün</p>
    <p class="line address address--4">Switzerland</p>

    <div class="contact-icons">
      <svg viewBox="0 0 24 24" aria-label="Phone" role="img">
        <circle cx="12" cy="12" r="12" fill="#b0193f"/>
        <path d="M6.5 10.5c0-2 2.5-3 5.5-3s5.5 1 5.5 3l-2 .6-.6-1.6c-1.8-.5-4-.5-5.8 0l-.6 1.6z" fill="#fff"/>
        <path d="M8.5 12h7l1 4.5h-9z" fill="#fff"/>
        <circle cx="12" cy="14" r="1.2" fill="#b0193f"/>
      </svg>
      <svg viewBox="0 0 24 24" aria-label="Email" role="img">
        <circle cx="12" cy="12" r="12" fill="#b0193f"/>
        <rect x="6.5" y="8" width="11" height="8" fill="#fff"/>
        <path d="M6.5 8l5.5 4.5L17.5 8M6.5 16l4-4M17.5 16l-4-4" fill="none" stroke="#b0193f" stroke-width="1"/>
      </svg>
      <svg viewBox="0 0 24 24" aria-label="Website" role="img">
        <circle cx="12" cy="12" r="12" fill="#b0193f"/>
        <path d="M11 9.5l1.8-1.8a2.3 2.3 0 0 1 3.3 3.3L14.3 12.8M13 14.5l-1.8 1.8a2.3 2.3 0 0 1-3.3-3.3L9.7 11.2M10 14l4-4" fill="none" stroke="#fff" stroke-width="1.3" stroke-linecap="round"/>
      </svg>
    </div>

    <p class="line contact contact--phone">+41 (0) 800 24 36 58</p>
    <p class="line contact contact--mail">hallo@wolkenbachtal.ch</p>
    <p class="line contact contact--web">www.<span class="domain">wolkenbachtal</span>.ch</p>
    <div class="rule rule--bottom"></div>
  </section>

  <section class="card card--back" aria-label="Business card back">
    <p class="line brand-name">Wolkenbachtal</p>
    <p class="line brand-tag">BEAUTY CLINIC</p>
    <p class="line web">wolkenbachtal.ch</p>
  </section>
</body>
</html>
```